Business Advisory Firm Business Card

A clean, very upscale looking business card. Not crowded.

Please include logo (attached) and:

Daria K. Pellworth
Four Marlow Court
New York, NY 10023
tel: (917) 555-0143
fax: (646) 555-0172
email: dpellworth@quarrystoneconsultants.example
website: www.quarrystoneconsultants.example

Target Market(s)

Business clients. Often real estate development firms, other advisory firms or growing companies that need assistance. I would like a card that looks impressive and confident.

Industry/Entity Type

Business

Colors

Designer to choose colors to be used in the design.

Requirements
Must have
• Impressive and confident. Please include logo.
Should not have
• nothing flashy...

```html
<!DOCTYPE html>
<html lang="en">
<head>
<meta charset="utf-8">
<title>Quarrystone Advisory Services – Business Card</title>
<link href="https://fonts.googleapis.com/css2?family=Montserrat:wght@300;400;600&display=swap" rel="stylesheet">
<style>
  :root {
    --page-bg: #e9e9e7;
    --card-bg: #f7f7f5;
    --card-shade: #e6e6e3;
    --ink: #2c2c2c;
    --ink-soft: #5a5a5a;
    --accent: #78b833;
  }
  html, body {
    margin: 0;
    width: 1200px;
    height: 800px;
    overflow: hidden;
    background: var(--page-bg);
    font-family: "Montserrat", Arial, sans-serif;
  }
  .business-card {
    position: absolute;
    left: 100px;
    top: 114px;
    width: 1000px;
    height: 572px;
    background:
      radial-gradient(ellipse 70% 90% at 0% 100%, var(--card-shade) 0%, rgba(230,230,227,0) 70%),
      var(--card-bg);
    box-shadow: 0 6px 24px rgba(0,0,0,0.12);
    overflow: hidden;
  }
  .firm-name {
    position: absolute;
    top: 52px;
    right: 66px;
    display: flex;
    align-items: flex-start;
    gap: 16px;
  }
  .firm-name__mark {
    width: 22px;
    height: 22px;
    margin-top: 6px;
    background: var(--accent);
  }
  .firm-name__text {
    margin: 0;
    font-weight: 600;
    font-size: 30px;
    line-height: 1.08;
    letter-spacing: 0.5px;
    text-transform: uppercase;
    color: var(--ink);
  }
  .holder-name {
    position: absolute;
    left: 310px;
    right: 0;
    top: 252px;
    display: flex;
    align-items: center;
    margin: 0;
    font-weight: 300;
    font-size: 56px;
    color: var(--ink);
  }
  .holder-name__given {
    padding-right: 14px;
    white-space: nowrap;
  }
  .holder-name__surname {
    flex: 1;
    padding: 2px 0 4px 12px;
    background: var(--accent);
    color: #fff;
    white-space: nowrap;
  }
  .contact-details {
    position: absolute;
    left: 80px;
    bottom: 50px;
    margin: 0;
    font-weight: 400;
    font-size: 21px;
    line-height: 1.36;
    color: var(--ink-soft);
    font-style: normal;
  }
</style>
</head>
<body>
  <div class="business-card">
    <div class="firm-name">
      <span class="firm-name__mark"></span>
      <p class="firm-name__text">Quarrystone<br>Advisory<br>Services, Inc.</p>
    </div>

    <h1 class="holder-name">
      <span class="holder-name__given">Daria K.</span>
      <span class="holder-name__surname">Pellworth</span>
    </h1>

    <address class="contact-details">
      Four Marlow Court<br>
      New York, NY 10023<br>
      tel: (917) 555-0143<br>
      fax: (646) 555-0172<br>
      email: dpellworth@quarrystoneconsultants.example<br>
      website: www.quarrystoneconsultants.example
    </address>
  </div>
</body>
</html>
```